Women Web Portal

We are developing an internet portal with content created by and for women in Latin America.
This portal will contain different categories focused on relevant topics for women who are at the same time mothers, lovers, workers, pet-owners, ...

We are looking for design that are at the same time uncluttered, easy-to-use and obvious, and comfy. Pastel colours, buttons using traditional fonts, large space for pictures, highlighted social elements,...

Our target being the middle-class women, we want a design that feels comfortable, real, a bit trendy and traditional, not a Tarsk & Welmore design, something women can relate to and feel comfortable enough to come back and participate.

Examples of websites:
www.dishtable.example
mujer.qelvo.example
www.cabellorinva.example
www.fourneau.example
Updates

Hi dear designers. After viewing some first drafts, I have updated the brief so you might have a better understanding of what we are looking for.

Thanks

Reason: We've been away for a while, unavailable to provide adequate feedback to the designs already sent. So we're extending the deadline in order to give time to everyone to adapt their work according to the feedback we'll be providing today.

Target Market(s)

Women between 25 and 50 years from Latin America. Mainly mothers: basically, we want women to interact with each other and with the content of the site so they create a strong community.

Advertisingly speaking, we want to have users, contents and FMCG brands to live together on this website.

Industry/Entity Type

Internet

Requirements
Must have
• Pastel colours for category tabs. Comfortable look & feel.

The design should include 3 different pages:
- Homepage
- Article page
- User profile

The page will be done in responsive design, so design should be thought to be adapted according to the browser (2 or 3 columns).

Thanks for doing it as a PSD file .

The design should also include:
- 8 category tabs
- Space for 728x90px and 300x600px advertising format.
- A relevant menu bar at the beginning of each page
Nice to have
• News feed/best content/most active comments zone: we need to bring forward content to our users so they'll be attracted to visit more pages of the website.

Small format to register (account).

Slider or any other moving objects.

Any idea that would facilitate and increase user participation
Should not have
• Actual text. please use Lorem Ipsum.

```html
<!DOCTYPE html>
<html lang="en">
<head>
<meta charset="utf-8">
<title>Entrellas — Women Web Portal</title>
<link href="https://fonts.googleapis.com/css2?family=Arimo:wght@400;700&display=swap" rel="stylesheet">
<style>
:root{
  --navy:#17365f;
  --navy-dark:#0f2747;
  --orange:#f6931e;
  --sky:#dbe8f5;
  --sky-line:#b9cfe6;
  --blue:#2d6cb5;
  --text:#333;
  --muted:#777;
  --white:#fff;
  --page:#ffffff;
}
*{box-sizing:border-box;margin:0;padding:0}
html,body{width:822px;height:1200px;overflow:hidden;background:var(--page)}
body{font-family:"Arimo",Arial,sans-serif;color:var(--text);font-size:10px;line-height:1.4;position:relative}
a{color:inherit;text-decoration:none}

/* header */
.masthead{height:84px;background:var(--navy);position:relative}
.account-links{position:absolute;left:28px;top:6px;color:#cfe0f3;font-size:9px}
.brand{position:absolute;left:28px;top:22px;color:var(--white);font-size:32px;font-weight:700;letter-spacing:-.5px}
.brand small{position:absolute;right:0;top:38px;font-size:10px;font-weight:400}
.search{position:absolute;right:28px;top:30px;display:flex}
.search span{width:170px;height:22px;background:var(--white);border-radius:2px 0 0 2px}
.search b{height:22px;padding:0 10px;background:var(--orange);color:var(--white);font-size:10px;line-height:22px;border-radius:0 2px 2px 0}

/* nav */
.main-nav{height:22px;background:var(--white);border-bottom:1px solid var(--sky-line);display:flex;padding-left:28px}
.main-nav a{padding:0 11px;font-size:9.5px;font-weight:700;line-height:22px;color:var(--navy)}
.main-nav a.is-active{background:var(--blue);color:var(--white)}
.sub-nav{height:22px;background:var(--sky);display:flex;padding-left:28px}
.sub-nav a{padding:0 10px;font-size:9px;line-height:22px;color:var(--navy);border-right:1px solid var(--sky-line)}

/* leaderboard */
.leaderboard{position:absolute;left:160px;top:140px;width:500px;height:58px;background:linear-gradient(90deg,#e9f3fb,#bcd9f1);display:flex;align-items:center;justify-content:space-between;padding:0 18px}
.leaderboard h3{font-size:24px;color:var(--navy);letter-spacing:-.5px}
.leaderboard h3 em{font-style:normal;color:var(--orange)}
.leaderboard .drill{background:var(--navy);color:var(--white);font-size:12px;font-weight:700;padding:8px 10px}

/* main */
.main{position:absolute;left:28px;top:210px;width:492px}
.slider{display:flex;gap:4px;height:200px}
.slide-hero{position:relative;width:368px;height:200px;background:linear-gradient(135deg,#c8b59b,#8f7b62 60%,#5d4f40)}
.slide-hero figcaption{position:absolute;left:0;right:0;bottom:0;background:rgba(0,0,0,.6);color:var(--white);padding:8px 10px}
.slide-hero figcaption strong{display:block;font-size:15px}
.slide-hero figcaption span{font-size:9px}
.slide-thumbs{display:flex;flex-direction:column;gap:4px;width:120px}
.slide-thumbs div{flex:1;position:relative;background:linear-gradient(135deg,#9cc3e3,#4f86b8)}
.slide-thumbs div:nth-child(2){background:linear-gradient(135deg,#e7c3a8,#b07a5e)}
.slide-thumbs div:nth-child(3){background:linear-gradient(135deg,#c9d9a2,#7f9a5a)}
.slide-thumbs span{position:absolute;left:0;right:0;bottom:0;background:rgba(0,0,0,.55);color:var(--white);font-size:8px;padding:3px 5px}
.article-title{font-size:13px;color:var(--text);margin:14px 0 6px}
.main p{font-size:8.5px;color:#555;margin-bottom:8px}
.section-title{font-size:12px;margin:16px 0 6px;color:var(--text)}
.video{position:relative;height:226px;background:linear-gradient(160deg,#d7d2c8,#9b958a 55%,#5f5a52)}
.video-bar{position:absolute;left:0;right:0;bottom:0;height:22px;background:rgba(20,20,20,.8)}
.video-bar i{position:absolute;left:40px;right:80px;top:10px;height:3px;background:#666}
.video-bar i::before{content:"";position:absolute;left:0;top:0;width:30%;height:3px;background:var(--orange)}
.play{position:absolute;left:50%;top:50%;width:54px;height:54px;margin:-38px 0 0 -27px}

/* sidebar */
.sidebar{position:absolute;left:534px;top:210px;width:262px}
.news{border:1px solid var(--sky-line)}
.news h4{background:var(--sky);color:var(--navy);font-size:11px;padding:6px 8px}
.news ul{list-style:none;padding:4px 8px}
.news li{font-size:9px;padding:3px 0 3px 10px;border-bottom:1px dotted #ccc;position:relative;color:#444}
.news li::before{content:"›";position:absolute;left:0;color:var(--orange);font-weight:700}
.ad-box{margin-top:10px;height:168px;background:linear-gradient(160deg,#3c1f57,#1d5a3a);color:var(--white);padding:14px;position:relative}
.ad-box strong{display:block;font-size:18px;line-height:1.1}
.ad-box strong em{font-style:normal;color:#ffd54a;font-size:26px}
.ad-box .ad-btn{position:absolute;left:14px;bottom:36px;background:var(--orange);padding:5px 12px;font-weight:700;font-size:11px}
.ad-box .ad-url{position:absolute;right:14px;bottom:10px;font-size:10px}
.social-box{margin-top:10px;border:1px solid var(--sky-line)}
.social-box h4{background:var(--blue);color:var(--white);font-size:11px;padding:5px 8px}
.social-box .fans{padding:6px 8px;font-size:8.5px}
.faces{display:grid;grid-template-columns:repeat(5,1fr);gap:5px;padding:0 8px 8px}
.faces div{height:34px;background:#c4d3e4}
.faces div:nth-child(even){background:#e1cdbd}
.feed{margin-top:10px;border:1px solid var(--sky-line);padding:8px}
.feed h4{color:var(--navy);font-size:11px;margin-bottom:6px}
.feed p{font-size:8.5px;color:#555;margin-bottom:6px;padding-bottom:5px;border-bottom:1px dotted #ccc}
.feed .follow{font-size:9px;color:var(--blue);font-weight:700}

/* footer */
.footer{position:absolute;left:0;top:970px;width:822px;height:230px;background:var(--navy);color:#cfe0f3}
.footer-top{height:46px;display:flex;align-items:center;padding:0 28px;border-bottom:1px solid #2d4f7d}
.social-icons{display:flex;gap:6px;margin-right:16px}
.social-icons span{width:16px;height:16px;background:#4f79aa;border-radius:2px}
.footer-links{font-size:9px}
.footer-brand{margin-left:auto;color:var(--white);font-size:22px;font-weight:700}
.footer-cols{display:flex;padding:14px 28px;gap:36px}
.footer-cols h5{color:var(--white);font-size:10px;margin-bottom:5px}
.footer-cols li{list-style:none;font-size:8.5px;line-height:1.55}
.cards{display:grid;grid-template-columns:repeat(3,26px);gap:4px}
.cards span{height:16px;background:#e9eef5;border-radius:2px}
.copyright{position:absolute;left:28px;bottom:10px;font-size:8.5px}
</style>
</head>
<body>

<header class="masthead">
  <div class="account-links">New user? | Register | Sign in</div>
  <div class="brand">Entrellas<small>.com</small></div>
  <div class="search"><span></span><b>Search the Web</b></div>
</header>

<nav class="main-nav">
  <a class="is-active">Initiatives</a><a>Learning to be Happy</a><a>Jokes for Women</a><a>Beauty Tips</a><a>Recruit Coupons</a><a>Tips For the Home</a><a>Couple Relationship</a>
</nav>
<nav class="sub-nav">
  <a>Christmas</a><a>Find Your Ideal Partner</a><a>Gastronomy</a><a>News and more</a><a>Animated Gifs</a><a>Pets</a><a>Poetry</a><a>Our Partners</a>
</nav>

<aside class="leaderboard">
  <h3>Get Ready to <em>Stand Firm</em></h3>
  <span class="drill">Stand Firm Drill</span>
</aside>

<main class="main">
  <section class="slider">
    <figure class="slide-hero" role="img" aria-label="Photo of a woman writing in a notebook">
      <figcaption><strong>Instructions on gratitude</strong><span>Simply dummy text of the printing and typesetting industry.</span></figcaption>
    </figure>
    <div class="slide-thumbs">
      <div role="img" aria-label="Photo of a mother and child"><span>92 tips to be happy</span></div>
      <div role="img" aria-label="Photo of friends laughing"><span>92 tips to be happy</span></div>
      <div role="img" aria-label="Photo of a woman outdoors"><span>92 tips to be happy</span></div>
    </div>
  </section>

  <h2 class="article-title">Instructions on gratitude</h2>
  <p>Simply dummy text of the printing and typesetting industry. Lorem Ipsum has been the industry's standard dummy text ever since the 1500s, when an unknown printer took a galley of type and scrambled it to make a type specimen book. It has survived not only five centuries, but also the leap into electronic typesetting, remaining essentially unchanged. It was popularised in the 1960s with the release of sheets containing Lorem Ipsum passages.</p>
  <p>Simply dummy text of the printing and typesetting industry. Lorem Ipsum has been the industry's standard dummy text ever since the 1500s, when an unknown printer took a galley of type and scrambled it to make a type specimen book. It has survived not only five centuries.</p>

  <h3 class="section-title">Featured Videos</h3>
  <div class="video" role="img" aria-label="Video still of a woman in a kitchen">
    <svg class="play" viewBox="0 0 54 54"><circle cx="27" cy="27" r="26" fill="rgba(0,0,0,.55)" stroke="#fff" stroke-width="2"/><path d="M21 16 L40 27 L21 38Z" fill="#fff"/></svg>
    <div class="video-bar"><i></i></div>
  </div>
  <p style="margin-top:10px">Simply dummy text of the printing and typesetting industry. Lorem Ipsum has been the industry's standard dummy text ever since the 1500s, when an unknown printer took a galley of type and scrambled it to make a type specimen book. It has not only five centuries.</p>
  <p>But also the leap into electronic typesetting, remaining essentially unchanged. It was popularised in the 1960s with the release of sheets containing Lorem Ipsum passages, and more recently with desktop publishing software including versions of Lorem Ipsum.</p>
</main>

<aside class="sidebar">
  <section class="news">
    <h4>LATEST NEWS</h4>
    <ul>
      <li>Ideas for a busy day</li>
      <li>Why be happy every morning</li>
      <li>Diabetes type 2: what is the risk</li>
      <li>Experiences and its essence</li>
      <li>Do you always love a cat?</li>
      <li>How are women emotionally?</li>
      <li>Formalities required to register the newly</li>
      <li>Five "love" of cats is good for you</li>
    </ul>
  </section>

  <section class="ad-box">
    <strong>PLAY<br><em>RUMMY</em><br>A GAME OF SKILL</strong>
    <span class="ad-btn">Play Now</span>
    <span class="ad-url">cardtable.example</span>
  </section>

  <section class="social-box">
    <h4>Circlebook</h4>
    <div class="fans">10,000 people like Entrellas</div>
    <div class="faces" role="img" aria-label="Grid of member profile photos">
      <div></div><div></div><div></div><div></div><div></div>
      <div></div><div></div><div></div><div></div><div></div>
    </div>
  </section>

  <section class="feed">
    <h4>Entrellas.com</h4>
    <p>Lorem ipsum why your account could be hidden as we are all your home life.</p>
    <p>Lorem ipsum dolor sit amet to play the lost on what do you see today friends.</p>
    <p>Simply dummy text of the printing and typesetting.</p>
    <span class="follow">Follow us on Chirpline</span>
  </section>
</aside>

<footer class="footer">
  <div class="footer-top">
    <div class="social-icons"><span></span><span></span><span></span><span></span></div>
    <div class="footer-links">Site Map | Search Terms | Advanced Search | Orders and Returns | Contact Us</div>
    <div class="footer-brand">Entrellas</div>
  </div>
  <div class="footer-cols">
    <ul><h5>Customer Service</h5><li>Returns</li><li>Shipping Options</li><li>Discount Codes</li><li>Privacy</li><li>Contact Us</li></ul>
    <ul><h5>What's New</h5><li>New Products</li><li>Featured</li><li>Products A-Z</li><li>Gift Vouchers</li><li>Buy a Gift Card</li></ul>
    <ul><h5>Other Sites</h5><li>Blog</li><li>Newsletter</li><li>Tables</li><li>Header Title</li><li>Toolbar</li></ul>
    <div><h5>Easy payment</h5><div class="cards"><span></span><span></span><span></span><span></span><span></span><span></span></div></div>
    <ul><h5>Need Help</h5><li>000 1234 567</li><li>Company Inc.</li><li>100 Sample Street</li><li>Lorem City 0000</li></ul>
  </div>
  <div class="copyright">Copyright © 2013 entrellas.example. All Rights Reserved.</div>
</footer>

</body>
</html>
```